Prestige Car Bodyshop Business Card

We are a car bodyshop based in the UK. Our customer base is mainly prestige high-value vehicles. I am looking for a classy and stylish business card design for my staff to give out to customers, with their direct email and phone number, as well as our main email and phone number with address details

I am also looking to have a general business card design with just our main company address and contact details, but also have a space to add a manufacturer approval logo (i.e Velmora, Orek, Tovalo etc... logo) in the corner somewhere.

I do not particularly want any outlines or pictures of cars on the card, I would just like a quality high-end look.

Please feel free to get in touch if you have any questions or queries?

Many Thanks

Malcolm

Target Market(s)

Prestige vehicle owners

Industry/Entity Type

Automotive

Contact Information for Business Card

I am looking for a classy and stylish business card design for my staff to give out to customers, with their direct email and phone number, as well as our main email and phone number with address details

Font styles to use
Sans Serif

Colors

Designer to choose colors to be used in the design.

Requirements
Nice to have
• I do not particularly want any outlines or pictures of cars on the card, I would just like a quality high-end look.

```html
<!DOCTYPE html>
<html lang="en">
<head>
<meta charset="utf-8">
<title>Halden Accident Repair Centre – Business Card</title>
<link rel="stylesheet" href="https://fonts.googleapis.com/css2?family=Open+Sans:wght@300;400;700&display=swap">
<style>
  :root {
    --stage: #e9e6e1;
    --blue-light: #0f68b3;
    --blue-deep: #1d3b80;
    --navy: #1f3a7a;
    --orange: #f07f1c;
    --ink: #2b2b2b;
    --rule: #c9c9c9;
    --white: #ffffff;
  }
  * { box-sizing: border-box; margin: 0; padding: 0; }
  html, body { width: 1200px; height: 1000px; overflow: hidden; }
  body {
    background: var(--stage);
    font-family: "Open Sans", sans-serif;
    position: relative;
  }
  .card {
    position: absolute;
    left: 265px;
    width: 667px;
    height: 397px;
    border-radius: 24px;
    overflow: hidden;
    box-shadow: 0 6px 18px rgba(0,0,0,.25);
  }
  /* Front */
  .card-front {
    top: 73px;
    background: radial-gradient(circle at 40% 10%, var(--blue-light), var(--blue-deep) 75%);
  }
  .front-disc {
    position: absolute;
    left: 22px; top: 17px;
    width: 360px; height: 360px;
    border-radius: 50%;
    background: linear-gradient(180deg, var(--blue-light), var(--blue-deep));
    box-shadow: 0 0 0 1px rgba(255,255,255,.08);
  }
  .front-brand {
    position: absolute;
    left: 408px; top: 258px;
    width: 228px;
    color: var(--white);
  }
  .front-brand .brand-word {
    font-weight: 300;
    font-size: 44px;
    line-height: 52px;
    letter-spacing: 0.5px;
  }
  .front-brand .brand-rule {
    height: 2px; background: var(--white); margin-top: 3px;
  }
  .front-brand .brand-sub {
    font-weight: 400;
    font-size: 16.5px;
    line-height: 22px;
    margin-top: 6px;
    white-space: nowrap;
  }
  /* Back */
  .card-back { top: 533px; background: var(--white); }
  .brand {
    position: absolute;
    left: 33px; top: 32px;
    display: flex; align-items: center; gap: 17px;
  }
  .brand-disc {
    width: 110px; height: 110px; border-radius: 50%;
    background: linear-gradient(180deg, var(--blue-light), var(--blue-deep));
  }
  .brand-text { color: var(--navy); width: 202px; }
  .brand-text .brand-word {
    font-weight: 300;
    font-size: 38px;
    line-height: 44px;
  }
  .brand-text .brand-rule { height: 2px; background: var(--navy); margin-top: 2px; }
  .brand-text .brand-sub {
    font-weight: 400;
    font-size: 14.5px;
    line-height: 20px;
    margin-top: 5px;
    white-space: nowrap;
  }
  .person {
    position: absolute;
    right: 32px; top: 170px;
    text-align: right;
  }
  .person-name { color: var(--orange); font-weight: 700; font-size: 19px; line-height: 26px; }
  .person-role { color: var(--ink); font-size: 15.5px; line-height: 20px; }
  .rule {
    position: absolute;
    left: 35px; top: 205px;
    width: 450px; height: 1px;
    background: var(--rule);
  }
  .contacts {
    position: absolute;
    left: 33px; top: 218px;
    list-style: none;
    color: var(--ink);
    font-size: 15.5px;
  }
  .contacts li { display: flex; align-items: center; gap: 7px; height: 24.5px; }
  .contacts svg { width: 15px; height: 15px; fill: var(--navy); }
  .address {
    position: absolute;
    right: 32px; top: 254px;
    text-align: right;
    color: var(--ink);
    font-size: 15.5px;
    line-height: 23px;
  }
  .wave { position: absolute; left: 0; bottom: 0; width: 667px; height: 90px; }
</style>
</head>
<body>

<section class="card card-front">
  <div class="front-disc"></div>
  <div class="front-brand">
    <p class="brand-word">HALDEN</p>
    <div class="brand-rule"></div>
    <p class="brand-sub">ACCIDENT REPAIR CENTRE</p>
  </div>
</section>

<section class="card card-back">
  <div class="brand">
    <div class="brand-disc"></div>
    <div class="brand-text">
      <p class="brand-word">HALDEN</p>
      <div class="brand-rule"></div>
      <p class="brand-sub">ACCIDENT REPAIR CENTRE</p>
    </div>
  </div>

  <div class="person">
    <p class="person-name">MAREN HOLLOWAY</p>
    <p class="person-role">Managing Director</p>
  </div>
  <div class="rule"></div>

  <ul class="contacts">
    <li><svg viewBox="0 0 16 16"><rect x="4" y="1" width="8" height="14" rx="1.5"/></svg>+ 000 000 0000</li>
    <li><svg viewBox="0 0 16 16"><path d="M2 6c0-2 3-3 6-3s6 1 6 3v1h-3V6H5v1H2z M4 8h8l1 6H3z"/></svg>+ 000 000 0000</li>
    <li><svg viewBox="0 0 16 16"><path d="M1 3h14v10H1z" /><path d="M1 3l7 6 7-6" fill="none" stroke="#fff" stroke-width="1.2"/></svg>maren@haldenrepair.com</li>
    <li><svg viewBox="0 0 16 16"><circle cx="8" cy="8" r="7"/><path d="M1 8h14M8 1c-3 4-3 10 0 14M8 1c3 4 3 10 0 14" fill="none" stroke="#fff" stroke-width="1"/></svg>www.haldenrepair.com</li>
  </ul>

  <p class="address">Level 29, 8 Arden Tower<br>Brackton, 20, New South Wales</p>

  <svg class="wave" viewBox="0 0 667 90" preserveAspectRatio="none">
    <path d="M0 10 C120 58 220 72 320 68 C450 62 540 10 667 6 L667 90 L0 90Z" fill="var(--orange)"/>
    <path d="M0 16 C120 64 220 78 320 74 C450 68 540 16 667 12 L667 90 L0 90Z" fill="var(--white)"/>
    <path d="M0 20 C120 68 220 82 320 78 C450 72 540 20 667 16 L667 90 L0 90Z" fill="var(--blue-light)"/>
    <path d="M0 38 C130 78 230 88 330 86 C460 82 550 36 667 30 L667 90 L0 90Z" fill="var(--blue-deep)"/>
  </svg>
</section>

</body>
</html>
```